Themed design for packaging sleeve and box

1) Gable box 330w x 200d x 160h (image attached for illustration purposes)
2) Sleeve to wrap around our food trays - see image attached

See the images uploaded!!!
This should not be copied, as some are from our competitors and are subject to Copywrite but gives an idea what kind of packaging we would be creating

From all the designs submitted, we will choose one final design and work with this designer to create our full packaging range.....

Target Market(s)

Working adults and health mined people

Font styles to use
Sans Serif

Colors

Designer to choose colors to be used in the design.

Requirements
Must have
• A clean modern look, striking design
Same design in different colours (see the drink bottles idea)
1) meat in shades of red
2) fish in shades of blue
3) vegetable in shades of green
Nice to have
• abstract white against strong colours
use shapes or mosaic or shades of the same colours
Should not have
• overpacked designs with too much information

```html
<!DOCTYPE html>
<html lang="en">
<head>
<meta charset="utf-8">
<title>Evenplate meal tray sleeves</title>
<link href="https://fonts.googleapis.com/css2?family=Oswald:wght@300;400;500&display=swap" rel="stylesheet">
<style>
  :root {
    --backdrop: #262626;
    --sleeve-white: #ffffff;
    --brand-green: #3dba2f;
    --veg: #1d7a48;
    --meat: #7b1409;
    --fish: #146f78;
    --badge-yellow: #f3b608;
    --badge-lime: #8dc73f;
    --ink: #111111;
    --text-light: #ffffff;
  }
  * { box-sizing: border-box; margin: 0; padding: 0; }
  html, body { width: 1200px; height: 957px; overflow: hidden; }
  body {
    background: var(--backdrop);
    font-family: "Oswald", "Arial Narrow", sans-serif;
    display: flex;
    align-items: center;
    justify-content: center;
    gap: 50px;
  }
  .sleeve {
    width: 320px;
    height: 567px;
    background: var(--sleeve-white);
    display: flex;
    flex-direction: column;
    --band: var(--veg);
  }
  .sleeve--meat { --band: var(--meat); }
  .sleeve--fish { --band: var(--fish); }

  .brand {
    height: 118px;
    display: flex;
    align-items: center;
    justify-content: center;
    gap: 10px;
  }
  .brand__name {
    font-size: 52px;
    font-weight: 400;
    color: var(--brand-green);
    letter-spacing: 1px;
    line-height: 1;
  }
  .brand__dot {
    width: 14px; height: 14px;
    border-radius: 50%;
    background: var(--brand-green);
  }

  .dish-photo {
    position: relative;
    height: 327px;
  }
  .dish-photo--noodles { background: radial-gradient(circle at 45% 50%, #c99a4a 0%, #8c9a3c 45%, #e9e9e7 75%); }
  .dish-photo--pork { background: radial-gradient(circle at 55% 45%, #5e8f2f 0%, #8a4a2a 50%, #e7e7e5 85%); }
  .dish-photo--salmon { background: radial-gradient(circle at 45% 50%, #e07a44 0%, #6c8f3a 40%, #efe8c2 65%, #ededeb 85%); }

  .prep-time {
    position: absolute;
    right: 0;
    bottom: 22px;
    width: 138px;
    height: 40px;
    background: var(--badge-yellow);
    display: flex;
    align-items: center;
    gap: 6px;
    padding-left: 8px;
  }
  .sleeve--fish .prep-time { background: var(--badge-lime); }
  .prep-time__num {
    width: 32px; height: 32px;
    border-radius: 50%;
    background: var(--ink);
    color: var(--badge-yellow);
    font-size: 20px;
    font-weight: 500;
    display: flex; align-items: center; justify-content: center;
  }
  .sleeve--fish .prep-time__num { color: var(--badge-lime); }
  .prep-time__label { color: var(--ink); line-height: 1; }
  .prep-time__label strong { display: block; font-size: 15px; font-weight: 400; }
  .prep-time__label span { font-size: 10.5px; font-weight: 300; }

  .info-band {
    flex: 1;
    background: var(--band);
    color: var(--text-light);
    padding: 12px 20px 0 25px;
    position: relative;
  }
  .dish-title { font-size: 23px; font-weight: 400; line-height: 1.05; }
  .dish-sub { font-size: 16px; font-weight: 300; line-height: 1.1; }

  .servings {
    position: absolute;
    right: 20px;
    top: 34px;
    width: 58px;
    text-align: center;
  }
  .servings svg { display: block; }
  .servings__num {
    position: absolute; left: 0; right: 0; top: 4px;
    font-size: 18px; font-weight: 500; color: var(--band); line-height: 1;
  }
  .servings__label {
    position: absolute; left: 0; right: 0; top: 25px;
    font-size: 7.5px; color: var(--band);
  }

  .claims {
    position: absolute;
    left: 22px;
    bottom: 20px;
    display: flex;
    gap: 8px;
    list-style: none;
  }
  .claim { width: 30px; text-align: center; font-size: 5px; line-height: 1.2; font-weight: 500; }
  .claim svg { display: block; margin: 0 auto 2px; }

  .storage {
    position: absolute;
    right: 20px;
    bottom: 22px;
    text-align: right;
    font-size: 8.5px;
    line-height: 1.45;
    font-weight: 400;
  }
</style>
</head>
<body>

<svg width="0" height="0" style="position:absolute">
  <defs>
    <symbol id="icon-leaf" viewBox="0 0 16 16">
      <circle cx="8" cy="8" r="7" fill="none" stroke="#fff" stroke-width="1"/>
      <path d="M8 12 C4 9 5 6 8 4 C11 6 12 9 8 12 Z M8 12 V6" fill="none" stroke="#fff" stroke-width="0.9"/>
    </symbol>
    <symbol id="icon-gf" viewBox="0 0 16 16">
      <circle cx="8" cy="8" r="7" fill="none" stroke="#fff" stroke-width="1"/>
      <text x="8" y="10.5" font-size="6.5" text-anchor="middle" fill="#fff" font-family="Oswald, sans-serif">GF</text>
    </symbol>
    <symbol id="icon-cloche" viewBox="0 0 58 40">
      <circle cx="29" cy="4" r="3" fill="#fff"/>
      <path d="M6 30 C6 14 16 6 29 6 C42 6 52 14 52 30 Z" fill="#fff"/>
      <rect x="1" y="30" width="56" height="8" rx="4" fill="#fff"/>
    </symbol>
  </defs>
</svg>

<article class="sleeve sleeve--veg">
  <header class="brand"><span class="brand__name">evenplate</span><span class="brand__dot"></span></header>
  <div class="dish-photo dish-photo--noodles" role="img" aria-label="Bowl of satay noodles with grilled tofu, edamame, chilli and fresh herbs">
    <div class="prep-time"><span class="prep-time__num">15</span><span class="prep-time__label"><strong>MINUTES</strong><span>prepare-to-plate</span></span></div>
  </div>
  <section class="info-band">
    <h2 class="dish-title">SATAY NOODLES</h2>
    <p class="dish-sub">WITH TOFU</p>
    <div class="servings"><svg width="58" height="40"><use href="#icon-cloche"/></svg><span class="servings__num">2</span><span class="servings__label">SERVINGS</span></div>
    <ul class="claims">
      <li class="claim"><svg width="16" height="16"><use href="#icon-leaf"/></svg>LOREM IPSUM</li>
      <li class="claim"><svg width="16" height="16"><use href="#icon-gf"/></svg>GLUTEN FREE</li>
      <li class="claim"><svg width="16" height="16"><use href="#icon-leaf"/></svg>NO ADDED PERSERVATIVE</li>
      <li class="claim"><svg width="16" height="16"><use href="#icon-leaf"/></svg>LOREM IPSUM</li>
    </ul>
    <p class="storage">KEEP REFRIGERATED<br>NET WT. 31.5 OZ. (1.97 LBS)</p>
  </section>
</article>

<article class="sleeve sleeve--meat">
  <header class="brand"><span class="brand__name">evenplate</span><span class="brand__dot"></span></header>
  <div class="dish-photo dish-photo--pork" role="img" aria-label="Grilled pork chop with spinach, grape and blue cheese salad">
    <div class="prep-time"><span class="prep-time__num">20</span><span class="prep-time__label"><strong>MINUTES</strong><span>prepare-to-plate</span></span></div>
  </div>
  <section class="info-band">
    <h2 class="dish-title">GRILLED PORK</h2>
    <p class="dish-sub">WITH SPINACH &amp; GRAPE SALAD</p>
    <div class="servings"><svg width="58" height="40"><use href="#icon-cloche"/></svg><span class="servings__num">3+</span><span class="servings__label">SERVINGS</span></div>
    <ul class="claims">
      <li class="claim"><svg width="16" height="16"><use href="#icon-leaf"/></svg>LOREM IPSUM</li>
      <li class="claim"><svg width="16" height="16"><use href="#icon-gf"/></svg>GLUTEN FREE</li>
      <li class="claim"><svg width="16" height="16"><use href="#icon-leaf"/></svg>NO ADDED PERSERVATIVE</li>
      <li class="claim"><svg width="16" height="16"><use href="#icon-leaf"/></svg>LOREM IPSUM</li>
    </ul>
    <p class="storage">KEEP REFRIGERATED<br>NET WT. 31.5 OZ. (1.97 LBS)</p>
  </section>
</article>

<article class="sleeve sleeve--fish">
  <header class="brand"><span class="brand__name">evenplate</span><span class="brand__dot"></span></header>
  <div class="dish-photo dish-photo--salmon" role="img" aria-label="Two pan-seared salmon fillets in creamy garlic sauce with spinach">
    <div class="prep-time"><span class="prep-time__num">20</span><span class="prep-time__label"><strong>MINUTES</strong><span>prepare-to-plate</span></span></div>
  </div>
  <section class="info-band">
    <h2 class="dish-title">ONE PAN SALMON</h2>
    <p class="dish-sub">WITH CREAMY GARLIC SPINACH</p>
    <div class="servings"><svg width="58" height="40"><use href="#icon-cloche"/></svg><span class="servings__num">2+</span><span class="servings__label">SERVINGS</span></div>
    <ul class="claims">
      <li class="claim"><svg width="16" height="16"><use href="#icon-leaf"/></svg>LOREM IPSUM</li>
      <li class="claim"><svg width="16" height="16"><use href="#icon-gf"/></svg>GLUTEN FREE</li>
      <li class="claim"><svg width="16" height="16"><use href="#icon-leaf"/></svg>NO ADDED PERSERVATIVE</li>
      <li class="claim"><svg width="16" height="16"><use href="#icon-leaf"/></svg>LOREM IPSUM</li>
    </ul>
    <p class="storage">KEEP REFRIGERATED<br>NET WT. 31.5 OZ. (1.97 LBS)</p>
  </section>
</article>

</body>
</html>
```